Quelvon Corporate General Presentation

Quelvon is a leading player in ICT (Information Communication Technology) cooling, we need a design for our corporate general presentation.

Attached is a reference of content

Our logo main color is industrial blue, our technology is green (energy saving).

existing website: www.quel-von.com www.quel-von.uk

Target Market(s)

Global

Industry/Entity Type

Communication

Number of Pages Required

5+ page

Font styles to use
Serif
Sans Serif

Colors
0255a3
3176b5
0293ce
33a6d7
9bcb3c

```html
<!DOCTYPE html>
<html lang="en">
<head>
<meta charset="UTF-8">
<title>Quelvon – Important Topics</title>
<link rel="stylesheet" href="https://fonts.googleapis.com/css2?family=Roboto:wght@700&family=Source+Sans+3:wght@400;600&display=swap">
<style>
  :root {
    --band-grey: #eaeef1;
    --row-grey: #eceff1;
    --logo-ring: #3aa8e0;
    --title-blue: #1ea6e2;
    --navy: #436296;
    --arrow-navy: #3f5f94;
    --accent-orange: #f6a623;
    --rule-dark: #3d5a86;
    --rule-light: #c9d6da;
    --text-slate: #4d5d6c;
    --logo-text: #3f5f94;
    --white: #ffffff;
  }
  * { box-sizing: border-box; margin: 0; padding: 0; }
  html, body { width: 1200px; height: 760px; overflow: hidden; background: var(--white); }
  .slide { position: relative; width: 1200px; height: 760px; overflow: hidden; background: var(--white); }
  .backdrop { position: absolute; inset: 0; }
  .brand-badge {
    position: absolute; left: 541px; top: 72px; width: 118px; height: 118px;
    border: 3px solid var(--logo-ring); border-radius: 50%; background: var(--white);
    display: flex; align-items: center; justify-content: center;
  }
  .brand-name {
    font-family: "Roboto", sans-serif; font-weight: 700; font-size: 21px;
    color: var(--logo-text); letter-spacing: 0.5px;
  }
  .slide-title {
    position: absolute; left: 0; width: 1200px; top: 222px; text-align: center;
    font-family: "Roboto", sans-serif; font-weight: 700; font-size: 36px;
    color: var(--title-blue); letter-spacing: 0.3px;
  }
  .topic-list { position: absolute; left: 459px; top: 306px; list-style: none; }
  .topic { display: flex; height: 43px; margin-bottom: 9px; }
  .topic-label {
    width: 243px; background: var(--row-grey); display: flex; align-items: center;
    padding-left: 30px; font-family: "Source Sans 3", sans-serif; font-size: 16px;
    color: var(--text-slate);
  }
  .topic-arrow {
    width: 47px; background: var(--arrow-navy);
    display: flex; align-items: center; justify-content: center;
  }
  .topic--active .topic-arrow { background: var(--accent-orange); }
</style>
</head>
<body>
<div class="slide">
  <svg class="backdrop" width="1200" height="760" viewBox="0 0 1200 760" aria-hidden="true">
    <polygon points="0,0 1200,0 1200,86 600,138 0,89" fill="var(--band-grey)"/>
    <line x1="0" y1="328" x2="1200" y2="328" stroke="var(--rule-dark)" stroke-width="1"/>
    <line x1="0" y1="379" x2="1200" y2="379" stroke="var(--rule-light)" stroke-width="1"/>
    <line x1="0" y1="429" x2="1200" y2="429" stroke="var(--rule-dark)" stroke-width="1"/>
    <line x1="0" y1="482" x2="1200" y2="482" stroke="var(--rule-light)" stroke-width="1"/>
    <polygon points="0,760 600,631 1200,760" fill="var(--navy)"/>
  </svg>

  <div class="brand-badge"><span class="brand-name">QUELVON</span></div>

  <h1 class="slide-title">IMPORTANT TOPICS</h1>

  <ul class="topic-list">
    <li class="topic topic--active">
      <span class="topic-label">Business &amp; strategy</span>
      <span class="topic-arrow"><svg width="14" height="12" viewBox="0 0 14 12"><path d="M1 6h10M7 1.5L11.5 6 7 10.5" fill="none" stroke="#fff" stroke-width="2.4" stroke-linecap="round" stroke-linejoin="round"/></svg></span>
    </li>
    <li class="topic">
      <span class="topic-label">Base situation</span>
      <span class="topic-arrow"><svg width="14" height="12" viewBox="0 0 14 12"><path d="M1 6h10M7 1.5L11.5 6 7 10.5" fill="none" stroke="#fff" stroke-width="2.4" stroke-linecap="round" stroke-linejoin="round"/></svg></span>
    </li>
    <li class="topic">
      <span class="topic-label">Product and solution</span>
      <span class="topic-arrow"><svg width="14" height="12" viewBox="0 0 14 12"><path d="M1 6h10M7 1.5L11.5 6 7 10.5" fill="none" stroke="#fff" stroke-width="2.4" stroke-linecap="round" stroke-linejoin="round"/></svg></span>
    </li>
    <li class="topic">
      <span class="topic-label">Key account</span>
      <span class="topic-arrow"><svg width="14" height="12" viewBox="0 0 14 12"><path d="M1 6h10M7 1.5L11.5 6 7 10.5" fill="none" stroke="#fff" stroke-width="2.4" stroke-linecap="round" stroke-linejoin="round"/></svg></span>
    </li>
  </ul>
</div>
</body>
</html>
```